Business cards for start-up accounting firm

I'm looking for a double sided business card ready for upload into Lumo print or similar print providers with no modification required by me.
I'm looking for something simple as i think cards that are too 'busy' actually detract from the message. I have some thoughts but more than happy to see what comes up. The logo i have came out of left field and i love it the moment i saw it!

My thoughts:

Side 1: Just the logo, perhaps on a dark grey or charcoal background to make the logo colours stand out?

Side 2: The call to action from me website 'Looking for a more relaxed, friendly and interactive relationship with your accountant?' with my contact information
Name: Gus Tarrow
Email: gus@ledgerowl.com.au
Website: www.ledgerowl.com.au
Phone: 1300 762 349

The call to action needs to be the first thing they see when they look at side 2. If it helps to know what we do and how we do it there is a draft website at www.ledgerowl.com.au

Like i said, happy to consider anything that comes up :)

Target Market(s)

i'm targeting small business owners who experience a lot of stress around finacial reporting and have had bad experiences with accountants in the past.

Industry/Entity Type

Accounting

Contact Information for Business Card

Contained in the Description

Font styles to use
Serif
Sans Serif
Other font styles liked:
• See logo files attached

Colors
474747

Requirements
Must have
• My logo, slogan and contact information

```html
<!DOCTYPE html>
<html lang="en">
<head>
<meta charset="utf-8">
<title>Ledger Owl – Business Cards</title>
<link rel="stylesheet" href="https://fonts.googleapis.com/css2?family=Montserrat:wght@300;400&family=Roboto:wght@400;500;700&display=swap">
<style>
  :root {
    --backdrop: #dcdcdc;
    --card: #333333;
    --card-dark: #2b2b2b;
    --yellow: #f5cc14;
    --white: #ffffff;
    --text-soft: #f0f0f0;
  }
  * { box-sizing: border-box; margin: 0; padding: 0; }
  html, body { width: 1200px; height: 1200px; overflow: hidden; }
  body {
    background: var(--backdrop);
    position: relative;
    font-family: "Roboto", Arial, sans-serif;
  }
  .card {
    position: absolute;
    left: 235px;
    width: 730px;
    height: 416px;
    overflow: hidden;
  }
  .card--front { top: 134px; }
  .card--back { top: 650px; }
  .card__pattern {
    position: absolute;
    inset: 0;
    background: linear-gradient(135deg, var(--card) 0%, var(--card-dark) 50%, var(--card) 100%);
  }

  /* Front */
  .brand {
    position: absolute;
    inset: 0;
    display: flex;
    align-items: center;
    justify-content: center;
  }
  .brand__name {
    font-family: "Roboto", Arial, sans-serif;
    font-weight: 700;
    font-size: 60px;
    line-height: 1;
    color: var(--yellow);
    letter-spacing: 1px;
  }

  /* Back */
  .pitch {
    position: absolute;
    left: 37px;
    top: 40px;
    width: 428px;
    font-family: "Montserrat", Arial, sans-serif;
    font-weight: 300;
    font-size: 22px;
    line-height: 28px;
    color: var(--white);
  }
  .person {
    position: absolute;
    left: 35px;
    top: 196px;
    display: flex;
    align-items: center;
    gap: 22px;
  }
  .person__name {
    font-weight: 700;
    font-size: 34px;
    color: var(--yellow);
    letter-spacing: 0.2px;
  }
  .contacts {
    position: absolute;
    left: 35px;
    top: 254px;
    list-style: none;
  }
  .contacts__item {
    display: flex;
    align-items: center;
    gap: 24px;
    height: 34.5px;
    font-size: 22px;
    color: var(--text-soft);
  }
  .icon { width: 20px; height: 20px; flex: none; }
  .services {
    position: absolute;
    left: 459px;
    top: 260px;
    list-style: none;
    color: var(--white);
    font-weight: 700;
    font-size: 20px;
    line-height: 24.5px;
  }
  .services__item--small { font-weight: 500; font-size: 17px; line-height: 20px; }
</style>
</head>
<body>

<section class="card card--front" aria-label="Card front">
  <div class="card__pattern" role="img" aria-label="Dark charcoal background with a subtle diamond tile pattern"></div>
  <div class="brand">
    <div class="brand__name">LEDGER OWL</div>
  </div>
</section>

<section class="card card--back" aria-label="Card back">
  <div class="card__pattern" role="img" aria-label="Dark charcoal background with a subtle diamond tile pattern"></div>

  <p class="pitch">Looking for a more relaxed, friendly and interactive relationship with your accountant?</p>

  <div class="person">
    <svg class="icon" viewBox="0 0 20 20" aria-hidden="true">
      <circle cx="10" cy="5.5" r="4.5" fill="var(--yellow)"/>
      <path d="M1 20 Q1 11 10 11 Q19 11 19 20 Z" fill="var(--yellow)"/>
    </svg>
    <span class="person__name">GUS TARROW</span>
  </div>

  <ul class="contacts">
    <li class="contacts__item">
      <svg class="icon" viewBox="0 0 20 20" aria-hidden="true">
        <rect x="1" y="4" width="18" height="13" rx="1" fill="none" stroke="var(--yellow)" stroke-width="1.8"/>
        <path d="M1.5 5 L10 11.5 L18.5 5" fill="none" stroke="var(--yellow)" stroke-width="1.8"/>
      </svg>
      <span>gus@ledgerowl.com.au</span>
    </li>
    <li class="contacts__item">
      <svg class="icon" viewBox="0 0 20 20" aria-hidden="true">
        <circle cx="10" cy="10" r="9" fill="var(--yellow)"/>
        <path d="M5 6 Q8 5 9 8 Q8 11 6 10 Z M11 12 Q14 11 15 14 Q13 16 11 15 Z" fill="var(--card)"/>
      </svg>
      <span>www.ledgerowl.com.au</span>
    </li>
    <li class="contacts__item">
      <svg class="icon" viewBox="0 0 20 20" aria-hidden="true">
        <path d="M4 1.5 L7 1 L8.5 5.5 L6.5 7.5 Q8.5 11.5 12.5 13.5 L14.5 11.5 L19 13 L18.5 16 Q17.5 19 14 18.5 Q3 15 1.5 5 Q1.5 2 4 1.5 Z" fill="var(--yellow)"/>
      </svg>
      <span>1300 762 349</span>
    </li>
  </ul>

  <ul class="services">
    <li class="services__item">Business Structuring</li>
    <li class="services__item">Smart Technology</li>
    <li class="services__item">Accounting &amp; Tax</li>
    <li class="services__item services__item--small">Business Advice &amp; Education</li>
  </ul>
</section>

</body>
</html>
```